Crane of the future landing page

Brindle Logic manufactures smart products for overhead cranes, the kind you find in manufacturing plants and warehouses. Our products collect data on how the cranes are used, and by who and connect the equipment to the cloud (think IOT for cranes). We provide notifications when things (are about to) go wrong as well as information used to ensure compliance with safety laws. Our product website is brindlelogic.com.au and you can see an example of the data here: http://www.brindlelogic.com.au/?userID=exampledata (nb, that link will go to a HTML 5 version of the site on a mobile device).
Next year we want to launch these products into the US market, and the theme of that launch will be "The Crane of the Future" We need a single HTML5 landing page that uses parallax scrolling to make the following points:

The crane of the future will be smart.
The crane of the future will be connected.
The crane of the future will cost less and last longer.

The crane of the future is here.

Register to learn more

We will provide copy and base pictures (please use stock images in the first cut) for these points.
Nb, an overhead crane looks like this http://www.pixmarrow.example/photo/big-crane-5820316?st=k41b772

This is a mobile crane https://www.liftwiki.example/wiki/Harvel_Lifting#/media/File:Tarn_Lifter_in_Tundra.jpg
This is a construction crane
http://railyard.fanpedia.example/wiki/Tower_Crane

Please only use images of overhead cranes

Target Market(s)

Industrial crane users, companies that supply and service overhead cranes

Industry/Entity Type

Digital

Coding

Coded - Design and coding required

Number of Pages Required

1 page

Font styles to use
Sans Serif

Requirements
Must have
• Image (maybe stylised) of a crane hoist ( this is the smart part of the crane) eg:
• http://www.veltrohoist.example/products/wire-rope-hoists
• It must show that our systems collect data from cranes and send this data, along with alerts, to mobile phones
• Parallax scrolling
• Name/email capture form
Nice to have
• Keep it simple and as uncluttered as possible.
• Full screen image background,maybe subtly animated
• Most people seem to visualise a hook when the think of cranes, maybe something like
• http://www.pixmarrow.example/photo/worker-standing-by-a-big-crane-hook-28391504?st=k41b772
• Reference to the fact that the information is available on your PC/Phone???
• For your background info, this link will open a flash based PC app, or a HTML version on mobile devices: http://www.brindlelogic.com.au/?userID=exampledata
• Something that indicates that you get email/sms notification when things go wrong.
Should not have
• It's hard because there aren't a lot of generic stock photos, but try to avoid brand names.
• Don't include a copy of the menu from our website. This is a landing page, the only place the BrindleLogic logo and a link to the website should appear is under the section: "The crane of the future is here"

```html
<!DOCTYPE html>
<html lang="en">
<head>
<meta charset="utf-8">
<title>The Crane of the Future — Brindle Logic</title>
<link rel="stylesheet" href="https://fonts.googleapis.com/css2?family=Montserrat:wght@400;600;700&display=swap">
<style>
  :root{
    --navy:#323651;
    --navy-deep:#2a2d45;
    --sky:#3a9be6;
    --sky-band:#3b97e8;
    --ring-blue:#2b9be0;
    --orange:#f7941d;
    --ink:#2f3450;
    --body-ink:#4a4d5e;
    --white:#ffffff;
    --arrow:#c9cbd3;
    --photo-light:#e9eaec;
    --photo-mid:#d2d4d8;
  }
  *{box-sizing:border-box;margin:0;padding:0}
  html,body{width:1200px;height:1000px;overflow:hidden;background:#ffffff}
  body{position:relative;font-family:"Montserrat",sans-serif;color:var(--ink)}
  .sprite{position:absolute;width:0;height:0;overflow:hidden}

  .view{position:absolute;top:0;height:1000px;overflow:hidden}
  .view--wide{left:0;width:610px;background:var(--navy)}
  .view--full{left:610px;width:590px;background:var(--navy);box-shadow:-4px 0 10px rgba(0,0,0,.25)}

  .abs{position:absolute}
  .hero{left:0;top:0;width:100%;background:linear-gradient(180deg,#f1f2f3 0%,var(--photo-light) 45%,var(--photo-mid) 100%)}
  .hoist{background:linear-gradient(160deg,#2f63c9 0%,#2a5fc0 55%,#f2b21d 85%,#e9a41a 100%);border-radius:0 0 40px 0;opacity:.92}
  .hand-phone{background:linear-gradient(150deg,#1c1d22 0%,#2c2f3a 40%,#d9a788 75%,#c99276 100%);border-radius:0 30px 30px 0}
  .savings-ring{border-radius:50%;background:radial-gradient(circle,#f7941d 0%,#f7a84a 30%,#ffffff 52%,#ffffff 80%,var(--ring-blue) 83%,var(--ring-blue) 100%)}

  .eyebrow{color:var(--sky);font-weight:700;text-transform:uppercase;letter-spacing:.02em;white-space:nowrap}
  .headline{font-weight:700;line-height:1.05;white-space:nowrap}
  .copy{font-weight:400;white-space:nowrap}
  .hero .headline,.hero-text .headline{color:var(--ink)}
  .hero-text .copy{color:var(--body-ink)}
  .on-dark .headline,.on-dark .copy{color:var(--white)}
  .features{list-style:none;color:var(--white);font-weight:600;white-space:nowrap}
  .features li::before{content:"";display:inline-block;width:.32em;height:.32em;border-radius:50%;background:var(--white);margin-right:.9em;vertical-align:middle}
  .cta{background:var(--sky);color:var(--white);font-weight:700;text-transform:uppercase;display:flex;align-items:center;justify-content:center;white-space:nowrap}
  .centered{text-align:center}
  .divider{height:1px;background:var(--sky);opacity:.75}
  .scroll-arrow{width:21px;height:21px;border-radius:50%;background:var(--arrow)}
  .chart{display:block}

  /* wide view */
  .view--wide .hero{height:330px}
  .view--wide .hoist{left:0;top:0;width:300px;height:290px}
  .view--wide .hero-text{left:403px;top:31px}
  .view--wide .hero-text .eyebrow{font-size:8.5px}
  .view--wide .hero-text .headline{font-size:16.5px;margin-top:6px}
  .view--wide .hero-text .copy{font-size:8.2px;line-height:11.4px;margin-top:6px}
  .view--wide .hand-phone{left:0;top:330px;width:300px;height:312px}
  .view--wide .chart{left:195px;top:486px;width:282px;height:138px}
  .view--wide .connected{left:403px;top:363px}
  .view--wide .connected .eyebrow{font-size:8px}
  .view--wide .connected .headline{font-size:15.5px;margin-top:6px}
  .view--wide .features{left:468px;top:426px;font-size:8px;line-height:12px}
  .view--wide .connected-cta{left:530px;top:473px;width:80px;height:21px;font-size:8px}
  .view--wide .divider{left:140px;top:665px;width:470px}
  .view--wide .savings{left:0;top:699px;width:802px}
  .view--wide .savings .eyebrow{font-size:8px}
  .view--wide .savings .headline{font-size:15px;margin-top:6px}
  .view--wide .savings .copy{font-size:8.2px;line-height:11.4px;margin-top:5px}
  .view--wide .savings-ring{left:314px;top:803px;width:176px;height:176px}

  /* full view */
  .view--full .hero{height:220px}
  .view--full .hoist{left:0;top:0;width:180px;height:192px}
  .view--full .hero-text{left:294px;top:20px}
  .view--full .hero-text .eyebrow{font-size:5.6px}
  .view--full .hero-text .headline{font-size:10.5px;margin-top:3px}
  .view--full .hero-text .copy{font-size:5.6px;line-height:8px;margin-top:4px}
  .view--full .hand-phone{left:0;top:218px;width:225px;height:220px}
  .view--full .chart{left:155px;top:323px;width:188px;height:92px}
  .view--full .connected{left:294px;top:241px}
  .view--full .connected .eyebrow{font-size:5.6px}
  .view--full .connected .headline{font-size:10.5px;margin-top:4px}
  .view--full .features{left:339px;top:283px;font-size:5.6px;line-height:8.3px}
  .view--full .connected-cta{left:381px;top:314px;width:54px;height:14px;font-size:5.4px}
  .view--full .divider-a{left:120px;top:442px;width:350px}
  .view--full .divider-b{left:120px;top:664px;width:350px}
  .view--full .savings{left:0;top:463px;width:590px}
  .view--full .savings .eyebrow{font-size:5.6px}
  .view--full .savings .headline{font-size:10.5px;margin-top:4px}
  .view--full .savings .copy{font-size:5.7px;line-height:7.8px;margin-top:3px}
  .view--full .savings-ring{left:236px;top:531px;width:118px;height:118px}
  .view--full .welcome{left:0;top:687px;width:590px}
  .view--full .welcome .eyebrow{font-size:5.6px}
  .view--full .welcome .headline{font-size:10px;margin-top:4px;color:var(--white)}
  .view--full .brand-disc{left:232px;top:736px;width:126px;height:126px;border-radius:50%;background:var(--white);display:flex;align-items:center;justify-content:center}
  .brand-name{font-weight:700;font-size:11px;color:var(--navy-deep);text-transform:uppercase;letter-spacing:.04em;white-space:nowrap}
  .view--full .arrow-1{left:551px;top:195px}
  .view--full .arrow-2{left:551px;top:415px}
  .view--full .arrow-3{left:551px;top:637px}
  .view--full .arrow-4{left:551px;top:861px}
  .view--full .signup{left:0;top:888px;width:590px;height:112px;background:var(--sky-band)}
  .signup .eyebrow{position:absolute;left:0;top:21px;width:100%;text-align:center;font-size:5.6px;color:#a9d3f5}
  .signup .headline{position:absolute;left:0;top:31px;width:100%;text-align:center;font-size:10.5px;color:var(--white)}
  .signup-field{position:absolute;top:60px;height:14px;background:var(--navy);border:0;color:#b9bccb;font-family:"Montserrat",sans-serif;font-size:5px;padding:0 5px;display:flex;align-items:center}
  .field-name{left:154px;width:89px}
  .field-email{left:253px;width:85px}
  .field-password{left:346px;width:88px}
  .signup-submit{position:absolute;left:252px;top:77px;width:85px;height:15px;border:1px solid var(--white);color:var(--white);font-weight:600;font-size:5px;display:flex;align-items:center;justify-content:center;text-transform:uppercase;white-space:nowrap}
</style>
</head>
<body>

<svg class="sprite" aria-hidden="true">
  <defs>
    <pattern id="chart-dots" width="5" height="5" patternUnits="userSpaceOnUse">
      <circle cx="1" cy="1" r=".55" fill="#ffffff" fill-opacity=".75"/>
    </pattern>
    <symbol id="analytics-chart" viewBox="0 0 282 138">
      <rect x="4" y="4" width="252" height="116" fill="url(#chart-dots)"/>
      <polyline points="52,47 75,71 120,50 165,81 209,62 253,9" fill="none" stroke="#f7941d" stroke-width="2.4"/>
      <polyline points="8,120 52,106 75,85 97,108 120,83 187,106 209,69 231,79 253,49" fill="none" stroke="#3a9be6" stroke-width="2.4"/>
      <g fill="#ffffff" stroke="#f7941d" stroke-width="2.2">
        <circle cx="52" cy="47" r="4"/><circle cx="75" cy="71" r="4"/><circle cx="120" cy="50" r="4"/>
        <circle cx="165" cy="81" r="4"/><circle cx="209" cy="62" r="4"/><circle cx="253" cy="9" r="5" fill="#f7941d" stroke="#ffffff" stroke-width="1.8"/>
      </g>
      <g fill="#ffffff" stroke="#3a9be6" stroke-width="2.2">
        <circle cx="8" cy="120" r="4"/><circle cx="52" cy="106" r="4"/><circle cx="75" cy="85" r="4"/>
        <circle cx="97" cy="108" r="4"/><circle cx="120" cy="83" r="4"/><circle cx="187" cy="106" r="4"/>
        <circle cx="209" cy="69" r="4"/><circle cx="231" cy="79" r="4"/><circle cx="253" cy="49" r="5" fill="#3a9be6" stroke="#ffffff" stroke-width="1.8"/>
      </g>
      <g fill="#ffffff" font-family="Montserrat, sans-serif" font-size="5">
        <text x="267" y="8">100%</text><text x="267" y="37">75%</text><text x="267" y="65">50%</text>
        <text x="267" y="93">25%</text><text x="267" y="122">0%</text>
      </g>
      <g fill="#ffffff" font-family="Montserrat, sans-serif" font-size="5" text-anchor="middle">
        <text x="8" y="133">Jan</text><text x="30" y="133">Feb</text><text x="52" y="133">Mar</text>
        <text x="75" y="133">Apr</text><text x="97" y="133">May</text><text x="120" y="133">Jun</text>
        <text x="142" y="133">Jul</text><text x="165" y="133">Aug</text><text x="187" y="133">Sep</text>
        <text x="209" y="133">Oct</text><text x="231" y="133">Nov</text><text x="253" y="133">Dec</text>
      </g>
    </symbol>
    <symbol id="down-arrow" viewBox="0 0 21 21">
      <circle cx="10.5" cy="10.5" r="10.5" fill="#c9cbd3"/>
      <path d="M10.5 5.5 V15 M6.8 11.4 L10.5 15 L14.2 11.4" fill="none" stroke="#ffffff" stroke-width="1.6" stroke-linecap="round" stroke-linejoin="round"/>
    </symbol>
  </defs>
</svg>

<!-- Wide view of the landing page -->
<section class="view view--wide">
  <div class="abs hero" role="img" aria-label="Black and white photo of a factory hall with overhead crane girders"></div>
  <div class="abs hoist" role="img" aria-label="Photo of a blue wire rope hoist with a yellow hook block"></div>
  <div class="abs hero-text">
    <p class="eyebrow">Intellectual Development</p>
    <h1 class="headline">The crane of the future will be<br>smart.</h1>
    <p class="copy">Lorem ipsum dolor sit amet, consectetur adipiscing elit.<br>Suspendisse varius enim in eros elementum tristique. Duis cursus,<br>mi quis viverra ornare, eros dolor interdum nulla, ut commodo<br>diam libero vitae erat. Aenean faucibus nibh et justo cursus id<br>rutrum lorem imperdiet. Nunc ut sem vitae risus tristique posuere.</p>
  </div>

  <svg class="abs chart" role="img" aria-label="Line chart of monthly crane usage"><use href="#analytics-chart"/></svg>
  <div class="abs hand-phone" role="img" aria-label="Photo of a hand holding a smartphone showing the monitoring app with a crane alert"></div>
  <div class="abs connected on-dark">
    <p class="eyebrow">The Most Advanced Analytics</p>
    <h2 class="headline">The crane of the future will be<br>connected.</h2>
  </div>
  <ul class="abs features">
    <li>24/7 Monitoring</li>
    <li>E-mail &amp; Text Alerts/Notifications</li>
    <li>Secure, Real-time Updates</li>
  </ul>
  <div class="abs cta connected-cta">Try it for free</div>

  <div class="abs divider"></div>
  <div class="abs savings on-dark centered">
    <p class="eyebrow">Save More. Do More</p>
    <h2 class="headline">The crane of the future will cost less and last longer.</h2>
    <p class="copy">Lorem ipsum dolor sit amet, consectetur adipiscing elit.<br>Suspendisse varius enim in eros elementum tristique. Duis cursus,<br>mi quis viverra ornare, eros dolor interdum nulla, ut commodo<br>diam libero vitae erat. Aenean faucibus nibh et justo cursus id<br>rutrum lorem imperdiet. Nunc ut sem vitae risus tristique posuere.</p>
  </div>
  <div class="abs savings-ring" role="img" aria-label="Illustration of an orange piggy bank with a dollar sign inside a blue and orange circular arrow"></div>
</section>

<!-- Full view of the landing page -->
<section class="view view--full">
  <div class="abs hero" role="img" aria-label="Black and white photo of a factory hall with overhead crane girders"></div>
  <div class="abs hoist" role="img" aria-label="Photo of a blue wire rope hoist with a yellow hook block"></div>
  <div class="abs hero-text">
    <p class="eyebrow">Intellectual Development</p>
    <h1 class="headline">The crane of the future will be<br>smart.</h1>
    <p class="copy">Lorem ipsum dolor sit amet, consectetur adipiscing elit.<br>Suspendisse varius enim in eros elementum tristique. Duis cursus,<br>mi quis viverra ornare, eros dolor interdum nulla, ut commodo<br>diam libero vitae erat. Aenean faucibus nibh et justo cursus id<br>rutrum lorem imperdiet. Nunc ut sem vitae risus tristique posuere.</p>
  </div>
  <svg class="abs scroll-arrow arrow-1" aria-hidden="true"><use href="#down-arrow"/></svg>

  <svg class="abs chart" role="img" aria-label="Line chart of monthly crane usage"><use href="#analytics-chart"/></svg>
  <div class="abs hand-phone" role="img" aria-label="Photo of a hand holding a smartphone showing the monitoring app with a crane alert"></div>
  <div class="abs connected on-dark">
    <p class="eyebrow">The Most Advanced Analytics</p>
    <h2 class="headline">The crane of the future will be<br>connected.</h2>
  </div>
  <ul class="abs features">
    <li>24/7 Monitoring</li>
    <li>E-mail &amp; Text Alerts/Notifications</li>
    <li>Secure, Real-time Updates</li>
  </ul>
  <div class="abs cta connected-cta">Try it for free</div>
  <svg class="abs scroll-arrow arrow-2" aria-hidden="true"><use href="#down-arrow"/></svg>

  <div class="abs divider divider-a"></div>
  <div class="abs savings on-dark centered">
    <p class="eyebrow">Save More. Do More</p>
    <h2 class="headline">The crane of the future will cost less and last longer.</h2>
    <p class="copy">Lorem ipsum dolor sit amet, consectetur adipiscing elit.<br>Suspendisse varius enim in eros elementum tristique. Duis cursus,<br>mi quis viverra ornare, eros dolor interdum nulla, ut commodo<br>diam libero vitae erat. Aenean faucibus nibh et justo cursus id<br>rutrum lorem imperdiet. Nunc ut sem vitae risus tristique posuere.</p>
  </div>
  <div class="abs savings-ring" role="img" aria-label="Illustration of an orange piggy bank with a dollar sign inside a blue and orange circular arrow"></div>
  <svg class="abs scroll-arrow arrow-3" aria-hidden="true"><use href="#down-arrow"/></svg>

  <div class="abs divider divider-b"></div>
  <div class="abs welcome centered">
    <p class="eyebrow">Welcome</p>
    <h2 class="headline">The crane of the future is here.</h2>
  </div>
  <div class="abs brand-disc"><span class="brand-name">Brindle Logic</span></div>
  <svg class="abs scroll-arrow arrow-4" aria-hidden="true"><use href="#down-arrow"/></svg>

  <form class="abs signup">
    <p class="eyebrow">Sign Up</p>
    <h2 class="headline">Getting started takes only a few seconds...</h2>
    <div class="signup-field field-name">Full name</div>
    <div class="signup-field field-email">Email Address</div>
    <div class="signup-field field-password">Password</div>
    <div class="signup-submit">Register to learn more</div>
  </form>
</section>

</body>
</html>
```